2020 Camp Thornbrook Golf Tournament

We are looking for someone to design our 2020 Golf Tournament brochure that we will mail out to participants. I have uploaded a document that gives details along with last year's document so that you can have a point of reference.

The flyer will need to be 8.5 x 11, portrait style on one side and landscape on the other side. All the information is included in the document that has been provided.

Target Market(s)

Golfers and hole sponsors

Industry/Entity Type

Recreation

Colors

Designer to choose colors to be used in the design.

Requirements
Must have
• Provided information on the document.
Nice to have
• Cool design
Should not have
• Cartoon art

```html
<!DOCTYPE html>
<html lang="en">
<head>
<meta charset="utf-8">
<title>Camp Thornbrook Benefit Golf Tournament</title>
<link href="https://fonts.googleapis.com/css2?family=Lato:ital,wght@0,400;0,700;0,900;1,400;1,700&family=Montserrat:wght@700;800&display=swap" rel="stylesheet">
<style>
:root{
  --stage:#2d2d2d;
  --lime:#72b844;
  --forest:#02664a;
  --ink:#1d1d1d;
  --paper:#ffffff;
  --mist:#e9ecea;
  --rule:#8a8a8a;
}
*{box-sizing:border-box;margin:0;padding:0}
html,body{width:1200px;height:1200px;overflow:hidden;background:var(--stage)}
body{position:relative;font-family:"Lato",sans-serif;color:var(--ink)}
.abs{position:absolute}

/* Portrait flyer */
.flyer{left:40px;top:262px;width:507px;height:710px;background:var(--paper);overflow:hidden}
.flyer-photo{left:0;top:0;width:270px;height:226px;clip-path:polygon(0 0,200px 0,268px 226px,0 226px);
  background:linear-gradient(160deg,#5f9fd6 0%,#9cc8e8 38%,#6fa05a 62%,#4c7f35 100%)}
.brand-mark{left:300px;top:38px;width:170px;display:flex;align-items:center;gap:6px;justify-content:center}
.brand-mark .dot{width:14px;height:14px;border-radius:50%;background:var(--forest);flex:none}
.brand-mark span{font:900 14px "Lato",sans-serif;color:var(--forest);letter-spacing:.5px}
.hero-band{left:0;top:0;width:507px;height:226px}
.hero-text{right:14px;top:110px;text-align:right;color:var(--paper);font-family:"Lato",sans-serif}
.hero-text .t1{font-weight:900;font-size:20px;line-height:20px}
.hero-text .t2{font-weight:900;font-size:14.5px;line-height:15px}
.hero-text .t3{font-weight:900;font-size:21px;line-height:22px;margin-top:7px}
.date-box{display:inline-block;background:var(--forest);padding:0 2px}
.hero-place{right:22px;top:186px;text-align:right;color:var(--paper);font-size:11px;line-height:14px}
.hero-pin{right:12px;top:190px}

.prices{left:0;top:226px;width:507px;height:102px;background:var(--mist);display:flex;border-bottom:1px solid var(--rule)}
.price{flex:1;text-align:center;padding-top:24px;position:relative;font-size:19px;line-height:20px}
.price+.price::before{content:"";position:absolute;left:0;top:8px;height:80px;border-left:1px solid var(--lime)}
.price b{display:block;color:var(--forest);font-weight:900;font-size:20px;line-height:22px}
.price:first-child{text-align:left;padding-left:21px;flex:.9}

.tax{left:0;top:328px;width:507px;height:68px;background:var(--mist);padding:11px 20px 0;font-style:italic;font-size:10.5px;line-height:14px}
.tax b{color:var(--forest);font-size:14px;font-weight:700}
.rules{left:0;top:393px;width:507px;height:6px;border-top:1.5px solid var(--ink);border-bottom:1.5px solid var(--ink)}
.pill{background:var(--lime);color:var(--paper);border-radius:14px;text-align:center}
.scramble{left:138px;top:383px;width:226px;height:26px;font-size:19px;line-height:26px}
.schedule{left:0;top:417px;width:507px;height:69px;background:var(--forest);color:var(--paper);font-size:11px}
.schedule .times{left:29px;top:13px;line-height:20px}
.schedule .times span{display:inline-block;width:36px}
.schedule .split{left:152px;top:8px;height:54px;border-left:1.5px solid var(--paper)}
.schedule .includes{left:166px;top:19px;width:330px;line-height:14px}
.contact-line{left:0;top:486px;width:507px;height:54px;background:var(--mist);text-align:center;padding-top:7px;font-style:italic;font-size:11px}
.contact-line b{font-weight:700}
.form-pill{left:99px;top:518px;width:325px;height:22px;font-size:14px;line-height:22px;font-style:italic;font-weight:700;border-radius:12px 12px 0 0;background:var(--forest)}
.form{left:0;top:540px;width:507px;height:157px;font-size:9.5px}
.form .split{left:267px;top:0;height:157px;border-left:1.5px solid var(--ink)}
.form h3{font-style:italic;font-weight:700;font-size:14.5px;margin-bottom:7px}
.col{top:15px}
.col.left{left:18px;width:232px}
.col.right{left:282px;width:212px}
.row{display:flex;gap:3px;height:15px;align-items:flex-end}
.row i{flex:1;border-bottom:.8px solid #555;margin-bottom:2px;font-style:normal}
.gap{height:5px}
.foot-strip{left:0;top:697px;width:507px;height:13px;background:var(--lime)}

/* Landscape card */
.card{left:583px;top:524px;width:579px;height:450px;overflow:hidden}
.card-photo{left:0;top:0;width:579px;height:450px;
  background:radial-gradient(ellipse at 72% 70%,#a8c76e 0%,#5c9a2c 30%,#3f7d1e 65%,#2f6414 100%)}
.card-title{left:18px;top:56px;color:var(--paper);font-family:"Montserrat",sans-serif;font-weight:800;line-height:1}
.card-title .c1{font-size:41px;letter-spacing:-.5px}
.card-title .c2{font-size:30px;letter-spacing:-.5px;margin-top:4px}
.card-date{left:24px;top:144px;color:var(--paper);font-family:"Montserrat",sans-serif;font-weight:800;font-size:28px}
.card-date .date-box{background:var(--lime);padding:0 4px}
.card-place{left:24px;top:188px;color:var(--paper);font-size:13px;display:flex;gap:8px;align-items:center}
.card-logo{left:13px;top:364px;width:89px;height:76px;background:var(--paper);display:flex;flex-direction:column;align-items:center;justify-content:center;gap:5px}
.card-logo .dot{width:12px;height:12px;border-radius:50%;background:var(--forest)}
.card-logo span{font:900 10px "Lato",sans-serif;color:var(--forest);text-align:center;line-height:12px}
.card-contact{left:111px;top:409px;width:363px;height:26px;border-radius:13px;background:#111;color:var(--paper);font-size:10px;font-weight:700;line-height:26px;text-align:center}
</style>
</head>
<body>

<section class="flyer abs">
  <div class="flyer-photo abs" role="img" aria-label="Golfer finishing a swing on a sunny course"></div>
  <svg class="hero-band abs" viewBox="0 0 507 226"><polygon points="229,98 507,98 507,226 268,226" fill="#72b844"/></svg>
  <div class="brand-mark abs"><i class="dot"></i><span>CAMP THORNBROOK</span></div>
  <div class="hero-text abs">
    <div class="t1">CAMP THORNBROOK</div>
    <div class="t2">BENEFIT GOLF TOURNAMENT</div>
    <div class="t3">APRIL <span class="date-box">3,</span> 2020</div>
  </div>
  <div class="hero-place abs">THE COURSE AT<br>WILLOW BEND (SEARCY, AR)</div>
  <svg class="hero-pin abs" width="10" height="14" viewBox="0 0 10 14"><path d="M5 0a5 5 0 0 1 5 5c0 3.5-5 9-5 9S0 8.5 0 5a5 5 0 0 1 5-5z" fill="#fff"/><circle cx="5" cy="5" r="2" fill="#72b844"/></svg>

  <div class="prices abs">
    <div class="price"><b>$400 Per</b>Four some</div>
    <div class="price"><b>$100 Per</b>Individual</div>
    <div class="price"><b>$400 Per</b>Hole<br>Sponsorships</div>
    <div class="price"><b>$5,000 Per</b>Tournament<br>Sponsor</div>
  </div>
  <div class="tax abs"><b>Tax info :</b> Camp Thornbrook is a 501(c)3 non-profit. Funds raised will be used to help provided scholarships and improve facilities.</div>
  <div class="rules abs"></div>
  <div class="scramble pill abs">Scramble Format</div>

  <div class="schedule abs">
    <div class="times abs"><div><span>11:30</span>Lunch</div><div><span>12:30</span>Shotgun Start</div></div>
    <div class="split abs"></div>
    <div class="includes abs"><b>Includes :</b> Lunch, 18 holes, cart, hole-in-one prize, closest to the pin contest, longest drive contest, and door prizes.</div>
  </div>
  <div class="contact-line abs">For more information call &#9743; <b>501-555-0142</b> or &#9993; <b>dana@campthornbrook.org.</b></div>
  <div class="form-pill pill abs">Camp Thornbrook Entry and Sponsorship Form</div>

  <div class="form abs">
    <div class="split abs"></div>
    <div class="col left abs">
      <h3>Team -- $400 or Individual -- $100</h3>
      <div class="row">Name <i></i></div>
      <div class="row">Address <i></i></div>
      <div class="row">City <i></i> St <i></i> Zip <i></i></div>
      <div class="row">Phone <i></i></div>
      <div class="row">Other Team Members <i></i></div>
      <div class="gap"></div>
      <div class="row">Carts&nbsp;&nbsp; Yes or No &nbsp;&nbsp; How many? <i></i></div>
      <div class="row">Check Enclosed &nbsp;&nbsp;&nbsp;&nbsp; Bill Me</div>
    </div>
    <div class="col right abs">
      <h3>Hole Sponsorships -- $100</h3>
      <div class="row">Name <i></i></div>
      <div class="row">Address <i></i></div>
      <div class="row">City <i></i> St <i></i> Zip <i></i></div>
      <div class="row">Phone</div>
      <div class="row">Name listed on your sign</div>
      <div class="gap"></div>
      <div class="row">Please mail check to Camp Thornbrook Golf</div>
      <div class="row">PO Box 4410; Searcy, AR 72143</div>
    </div>
  </div>
  <div class="foot-strip abs"></div>
</section>

<section class="card abs">
  <div class="card-photo abs" role="img" aria-label="Golf ball resting at the lip of the cup beside the flagstick on the green"></div>
  <div class="card-title abs">
    <div class="c1">CAMP THORNBROOK</div>
    <div class="c2">BENEFIT GOLF TOURNAMENT</div>
  </div>
  <div class="card-date abs">APRIL <span class="date-box">3</span> | 2020</div>
  <div class="card-place abs">
    <svg width="10" height="14" viewBox="0 0 10 14"><path d="M5 0a5 5 0 0 1 5 5c0 3.5-5 9-5 9S0 8.5 0 5a5 5 0 0 1 5-5z" fill="#fff"/><circle cx="5" cy="5" r="2" fill="#3f7d1e"/></svg>
    THE COURSE AT WILLOW BEND (SEARCY, AR)
  </div>
  <div class="card-logo abs"><i class="dot"></i><span>CAMP<br>THORNBROOK</span></div>
  <div class="card-contact abs">For more information call &#9743; 501-555-0142 or &#9993; dana@campthornbrook.org.</div>
</section>

</body>
</html>
```